I need a business card design for my new clinic (SPORTS MEDICINE OF KNEE). I am orthopedist, expert in sports surgery, especially knee surgery. I prefer, as colors, the colors of my logo (green, black and white). I already have my logo and should appear on my card. It's good to see my site to have ideas (www.drlucianovarela.com)
It needs contain:
my name: Dr. Luciano Varela
my registration: CRM 584-902
my specialty: Cirurgia do Joelho / Esporte
my address: Centro Executivo - Pinheiral Plaza
Av. Doutor Augusto Brandão Cunha, 2740 sala 0836
Jd. Ipanema - Ribeirão Preto - SP
my phone number: Tel (16) 8245-3908
my clinic phone: (16) 3670-4851
my e-mail: drlucianovarela@mailbox-exemplo.com
my site: www.drlucianovarela.com

Target Market(s)

futures patients

Industry/Entity Type

Clinic

Requirements
Nice to have
• letters not overfilled
straight lines, with few curves

```html
<!DOCTYPE html>
<html lang="pt-BR">
<head>
<meta charset="utf-8">
<title>VARELA – Cartões de Visita</title>
<link rel="stylesheet" href="https://fonts.googleapis.com/css2?family=Arimo:wght@400&family=Tinos:wght@400&display=swap">
<style>
  :root {
    --bg: #ecebe8;
    --green: #45bb7c;
    --green-deep: #3aa86e;
    --black: #1d1b1a;
    --white: #ffffff;
    --ink: #1a1a1a;
    --asphalt-a: #3a3a3a;
    --asphalt-b: #1f1f1f;
  }
  * { margin: 0; padding: 0; box-sizing: border-box; }
  html, body { width: 1200px; height: 733px; overflow: hidden; }
  body { background: var(--bg); position: relative; font-family: "Arimo", Arial, sans-serif; color: var(--ink); }

  .card { position: absolute; width: 428px; height: 244px; background: var(--white); border: 1px solid #444; overflow: hidden; }
  .card--diagonal { left: 137px; top: 81px; }
  .card--plain { left: 667px; top: 81px; }
  .card--panel { left: 137px; top: 387px; }
  .card--wave { left: 667px; top: 387px; }

  .card__shapes { position: absolute; inset: 0; width: 428px; height: 244px; }

  .brand { position: absolute; left: 5px; top: 5px; display: flex; align-items: center; gap: 10px; }
  .brand__mark { width: 36px; height: 36px; background: var(--green); border: 2px solid var(--black); border-radius: 4px; }
  .brand__name { font-family: "Tinos", "Times New Roman", serif; font-size: 31px; color: var(--black); letter-spacing: 0.5px; line-height: 1; }

  .reg { position: absolute; top: 12px; right: 10px; font-size: 13.5px; color: var(--black); }

  .info { position: absolute; font-size: 12px; line-height: 13px; }
  .info__row { display: flex; }
  .info__label { width: 70px; flex: none; }
  .info__gap { height: 22px; }

  .specialty { position: absolute; left: 5px; top: 211px; font-size: 12.5px; color: var(--white); line-height: 17px; }
  .band-mark { position: absolute; left: 364px; top: 204px; width: 40px; height: 36px; background: var(--white); border: 2px solid var(--black); border-radius: 4px; }
  .band-mark::after { content: ""; position: absolute; inset: 6px; background: var(--green); }
</style>
</head>
<body>

<section class="card card--diagonal">
  <svg class="card__shapes" viewBox="0 0 428 244">
    <polygon points="282,0 428,0 428,208 0,208 0,122" fill="var(--green)"/>
    <polygon points="282,0 300,0 0,134 0,122" fill="var(--black)"/>
    <rect x="0" y="208" width="428" height="22" fill="var(--black)"/>
    <rect x="0" y="210" width="428" height="18" fill="none" stroke="var(--white)" stroke-width="1.5"/>
  </svg>
  <div class="brand"><span class="brand__mark"></span><span class="brand__name">VARELA</span></div>
  <div class="reg">REG.- CRM 584-902</div>
  <div class="info" style="left:75px; top:104px;">
    <div class="info__row"><span class="info__label">Address:</span><span>Centro Executivo - Pinheiral Plaza<br>Av. Doutor Augusto Brandão Cunha,<br>2740 sala 0836 Jd. Ipanema - Ribeirão Preto - SP</span></div>
    <div class="info__gap"></div>
    <div class="info__row"><span class="info__label">Phone:</span><span>H(16) 8245-3908, O(16) 3670-4851</span></div>
    <div class="info__row"><span class="info__label">E-mail:</span><span>drlucianovarela@mailbox-exemplo.com</span></div>
    <div class="info__row"><span class="info__label">Web site:</span><span>&nbsp;www.drlucianovarela.com</span></div>
  </div>
  <div class="specialty">Specialty: Cirurgia do Joelho / Esporte</div>
  <div class="band-mark"></div>
</section>

<section class="card card--plain">
  <svg class="card__shapes" viewBox="0 0 428 244">
    <rect x="0" y="209" width="428" height="21" fill="var(--black)"/>
  </svg>
  <div class="brand"><span class="brand__mark"></span><span class="brand__name">VARELA</span></div>
  <div class="reg">Reg. CRM 584-902</div>
  <div class="info" style="left:55px; top:84px;">
    <div class="info__row"><span class="info__label">Address:</span><span>Centro Executivo - Pinheiral Plaza<br>Av. Doutor Augusto Brandão Cunha, 2740 sala 0836<br>Jd. Ipanema - Ribeirão Preto - SP</span></div>
    <div class="info__gap" style="height:35px"></div>
    <div class="info__row"><span class="info__label">Phone:</span><span>H(16) 8245-3908, O(16) 3670-4851</span></div>
    <div class="info__row"><span class="info__label">E-mail:</span><span>drlucianovarela@mailbox-exemplo.com</span></div>
    <div class="info__row"><span class="info__label">Web site:</span><span>&nbsp;www.drlucianovarela.com</span></div>
  </div>
  <div class="specialty">Specialty: Cirurgia do Joelho / Esporte</div>
  <div class="band-mark"></div>
</section>

<section class="card card--panel">
  <svg class="card__shapes" viewBox="0 0 428 244">
    <defs>
      <linearGradient id="asphalt" x1="0" y1="0" x2="1" y2="1">
        <stop offset="0" stop-color="var(--asphalt-a)"/>
        <stop offset="1" stop-color="var(--asphalt-b)"/>
      </linearGradient>
    </defs>
    <rect x="0" y="66" width="418" height="118" fill="url(#asphalt)" role="img" aria-label="Dark asphalt texture behind the contact panel"/>
    <polygon points="48,66 413,66 413,186 48,194 48,180 30,170 48,160 48,80 30,74" fill="var(--green)"/>
    <rect x="0" y="209" width="428" height="21" fill="var(--black)"/>
  </svg>
  <div class="brand"><span class="brand__mark"></span><span class="brand__name">VARELA</span></div>
  <div class="reg">REG. CRM 584-902</div>
  <div class="info" style="left:63px; top:84px;">
    <div class="info__row"><span class="info__label">Address:</span><span>Centro Executivo - Pinheiral Plaza<br>Av. Doutor Augusto Brandão Cunha,<br>2740 sala 0836 Jd. Ipanema - Ribeirão Preto - SP</span></div>
    <div class="info__gap"></div>
    <div class="info__row"><span class="info__label">Phone:</span><span>H(16) 8245-3908, O(16) 3670-4851</span></div>
    <div class="info__row"><span class="info__label">E-mail:</span><span>drlucianovarela@mailbox-exemplo.com</span></div>
    <div class="info__row"><span class="info__label">Web site:</span><span>&nbsp;www.drlucianovarela.com</span></div>
  </div>
  <div class="specialty">specialty: Cirurgia do Joelho / Esporte</div>
  <div class="band-mark"></div>
</section>

<section class="card card--wave">
  <svg class="card__shapes" viewBox="0 0 428 244">
    <path d="M0,172 C25,118 60,94 140,86 C250,76 340,66 385,52 C405,46 420,40 428,34 L428,244 L0,244 Z" fill="var(--green)"/>
    <path d="M0,172 C25,118 60,94 140,86 C250,76 340,66 385,52 C405,46 420,40 428,34" fill="none" stroke="var(--black)" stroke-width="5"/>
    <rect x="0" y="209" width="428" height="22" fill="var(--black)"/>
    <rect x="0" y="211" width="428" height="18" fill="none" stroke="var(--white)" stroke-width="1.5"/>
  </svg>
  <div class="brand"><span class="brand__mark"></span><span class="brand__name">VARELA</span></div>
  <div class="reg">REG. CRM 584-902</div>
  <div class="info" style="left:77px; top:104px;">
    <div class="info__row"><span class="info__label">Address:</span><span>Centro Executivo - Pinheiral Plaza<br>Av. Doutor Augusto Brandão Cunha,<br>2740 sala 0836 Jd. Ipanema - Ribeirão Preto - SP</span></div>
    <div class="info__gap" style="height:18px"></div>
    <div class="info__row"><span class="info__label">Phone:</span><span>H(16) 8245-3908, O(16) 3670-4851</span></div>
    <div class="info__row"><span class="info__label">E-mail:</span><span>drlucianovarela@mailbox-exemplo.com</span></div>
    <div class="info__row"><span class="info__label">Web site:</span><span>&nbsp;www.drlucianovarela.com</span></div>
  </div>
  <div class="specialty">Specialty: Cirurgia do Joelho / Esporte</div>
  <div class="band-mark"></div>
</section>

</body>
</html>
```